Building Company Brochure for New Clients

We need an A3 landscape brochure designed (preferably 2xA4 designs next to each other in case we want to fold the brochure in half) that will be sent to new and prospective clients. We are a Builder on the East Coast of Australia, we specialise in Custom Homes and Renovations and our focus is on communication and a high quality finish. We want to see designs that convey our tagline 'building a lifestyle'.

Our logo and the following details must be included:
Ph: 024719353 | 0413597264
info@harlowbuildgroup.example.au
www.harlowbuildgroup.example.au
facebook.com/harlowbuildgroup
(facebook and instagram icons)

There is also text content in an attached file as well as photos. Choose any that will fit with your design, please try and use a variety of the houses. The logos are attached in psd files - feel free to choose from either colour.

Target Market(s)

30 - 60 year old couples.

Industry/Entity Type

Residential Construction

Font styles to use
Other font styles liked:
• Nokia Pure; SF Automation; (these specifics plus a suitable general body text)

Requirements
Must have
• The Brochure must include the text in the attached file. Our logo and the following details must be included:
• Ph: 024719353 | 0413597264
• info@harlowbuildgroup.example.au
• www.harlowbuildgroup.example.au
• facebook.com/harlowbuildgroup
• (facebook and instagram icons)
Nice to have
• A variety of the houses featured. Colours to work with the logo.

```html
<!DOCTYPE html>
<html lang="en">
<head>
<meta charset="utf-8">
<title>Harlow Build Group – Brochure</title>
<link href="https://fonts.googleapis.com/css2?family=Titillium+Web:ital,wght@0,400;0,600;0,700;1,700&family=Open+Sans:wght@400;600;700&display=swap" rel="stylesheet">
<style>
  :root{
    --blue:#2f5f96;
    --navy:#1d3c66;
    --sky:#6a93c4;
    --ink:#2b2f36;
    --grey:#6b7078;
    --paper:#ffffff;
    --bg:#e4e5e7;
  }
  *{box-sizing:border-box;margin:0;padding:0}
  html,body{width:1200px;height:998px;overflow:hidden;background:var(--bg)}
  body{font-family:"Open Sans",Arial,sans-serif;color:var(--ink);position:relative}
  .spread{position:absolute;left:270px;width:660px;height:467px;background:var(--paper);box-shadow:0 4px 14px rgba(0,0,0,.18);overflow:hidden}
  .spread--outer{top:24px}
  .spread--inner{top:511px}
  .page{position:absolute;top:0;width:330px;height:467px;overflow:hidden}
  .page--left{left:0}
  .page--right{left:330px}
  .fold{position:absolute;left:329px;top:0;width:2px;height:467px;background:rgba(0,0,0,.06)}
  .layer{position:absolute;left:0;top:0}
  .brand{position:absolute;display:flex;align-items:center;gap:8px;font-family:"Titillium Web",Arial,sans-serif;font-weight:700;color:var(--navy);line-height:1}
  .brand__mark{width:16px;height:16px;background:var(--blue)}
  .brand--back{left:0;width:330px;top:130px;justify-content:center;font-size:26px;letter-spacing:1px}
  .brand--front{left:0;width:330px;top:26px;justify-content:center;font-size:17px;letter-spacing:1px}
  .brand__mark--small{width:11px;height:11px}
  .phones{position:absolute;left:0;width:330px;top:186px;display:flex;justify-content:center;align-items:center;gap:5px;font-family:"Titillium Web",Arial,sans-serif;font-weight:700;font-size:12px;color:var(--navy)}
  .contact-list{position:absolute;left:0;width:330px;top:206px;display:flex;justify-content:center;gap:10px;font-size:5.5px;color:var(--grey)}
  .contact-list span{display:flex;align-items:center;gap:3px}
  .tagline{position:absolute;right:24px;top:292px;text-align:right;font-family:"Titillium Web",Arial,sans-serif;line-height:.95}
  .tagline__lead{display:block;font-size:30px;font-weight:700;font-style:italic;color:var(--blue);letter-spacing:1px}
  .tagline__rest{display:block;font-size:25px;font-weight:400;color:var(--ink);letter-spacing:1px}
  .front-web{position:absolute;right:24px;top:354px;font-size:6.5px;color:var(--navy);font-weight:600}
  .intro{position:absolute;left:14px;top:200px;width:150px;font-family:"Titillium Web",Arial,sans-serif;font-size:11.5px;font-weight:600;line-height:1.2;color:#fff}
  .section{position:absolute;left:20px;width:290px}
  .section--build{top:318px}
  .section--reno{top:380px}
  .section__title{font-family:"Titillium Web",Arial,sans-serif;font-size:12.5px;font-weight:600;color:var(--blue);line-height:1.1}
  .section__sub{font-size:5.8px;font-weight:700;margin-top:2px}
  .section__text{font-size:5.5px;line-height:1.45;margin-top:2px;color:var(--ink)}
  .team{position:absolute;top:18px;left:18px;width:140px}
  .team__title{font-family:"Titillium Web",Arial,sans-serif;font-size:10.5px;font-weight:600;color:var(--blue)}
  .team__text,.consult{font-size:5.5px;line-height:1.45;margin-top:3px}
  .consult{position:absolute;top:18px;left:172px;width:140px;margin-top:0}
  .guarantee{position:absolute;top:80px;left:18px;width:150px}
  .guarantee__title{font-family:"Titillium Web",Arial,sans-serif;font-size:9.5px;font-weight:600;color:var(--blue)}
  .guarantee__list{list-style:none;margin-top:4px}
  .guarantee__list li{font-size:5.6px;font-weight:700;line-height:1.35;padding-left:7px;position:relative;margin-bottom:2px}
  .guarantee__list li::before{content:"";position:absolute;left:0;top:2.5px;width:3px;height:3px;background:var(--ink)}
  .guarantee__list--side{position:absolute;top:120px;left:185px;width:120px}
  .services{position:absolute;left:22px;top:350px;width:290px;color:#fff}
  .services__title{font-family:"Titillium Web",Arial,sans-serif;font-size:12px;font-weight:400;line-height:1.05;letter-spacing:.5px}
  .services__area{font-size:5.5px;margin-top:5px;opacity:.9}
  .services__licence{font-size:5px;margin-top:2px;opacity:.9}
  .services__phones{font-family:"Titillium Web",Arial,sans-serif;font-size:15px;font-weight:700;margin-top:9px}
  .services__web{font-size:6.5px;font-weight:600;margin-top:1px}
  .services__links{position:absolute;left:210px;top:60px;font-size:4.6px;line-height:1.8;opacity:.9}
</style>
</head>
<body>

<section class="spread spread--outer" aria-label="Brochure outside">
  <div class="page page--left back-cover">
    <svg class="layer" width="330" height="467" viewBox="0 0 330 467">
      <defs>
        <linearGradient id="washTone" x1="0" y1="0" x2="0" y2="1">
          <stop offset="0" stop-color="#dfe6ee"/>
          <stop offset="1" stop-color="#ffffff"/>
        </linearGradient>
      </defs>
      <rect role="img" aria-label="Faint wash of a coastal home exterior" x="0" y="0" width="330" height="260" fill="url(#washTone)" opacity=".7"/>
      <path d="M0 418 Q170 380 330 405 L330 467 L0 467Z" fill="var(--sky)" opacity=".55"/>
      <path d="M0 430 Q170 398 330 420 L330 467 L0 467Z" fill="var(--blue)"/>
      <path d="M0 448 Q170 420 330 442 L330 467 L0 467Z" fill="var(--navy)"/>
    </svg>
    <div class="brand brand--back"><span class="brand__mark"></span>HARLOW BUILD GROUP</div>
    <div class="phones">
      <svg width="10" height="10" viewBox="0 0 24 24" aria-hidden="true"><path fill="var(--navy)" d="M6.6 10.8a15 15 0 0 0 6.6 6.6l2.2-2.2a1 1 0 0 1 1-.25 11.4 11.4 0 0 0 3.6.57 1 1 0 0 1 1 1V20a1 1 0 0 1-1 1A17 17 0 0 1 3 4a1 1 0 0 1 1-1h3.5a1 1 0 0 1 1 1c0 1.25.2 2.45.57 3.57a1 1 0 0 1-.25 1z"/></svg>
      024719353, 0413597264
    </div>
    <div class="contact-list">
      <span>info@harlowbuildgroup.example.au</span>
      <span>www.harlowbuildgroup.example.au</span>
      <span>facebook.com/harlowbuildgroup</span>
    </div>
  </div>

  <div class="page page--right front-cover">
    <svg class="layer" width="330" height="467" viewBox="0 0 330 467">
      <defs>
        <linearGradient id="poolTone" x1="0" y1="0" x2="0" y2="1">
          <stop offset="0" stop-color="#9cc1e6"/>
          <stop offset=".55" stop-color="#e9ecef"/>
          <stop offset="1" stop-color="#2a9fd6"/>
        </linearGradient>
      </defs>
      <polygon points="0,78 330,60 330,66 0,86" fill="var(--blue)"/>
      <polygon role="img" aria-label="Photo of a white two-storey home with a pool and timber deck" points="0,90 330,70 330,245 0,285" fill="url(#poolTone)"/>
      <polygon points="0,285 330,245 330,252 0,294" fill="var(--navy)"/>
      <path d="M0 410 Q170 378 330 400 L330 467 L0 467Z" fill="var(--sky)" opacity=".55"/>
      <path d="M0 425 Q170 395 330 418 L330 467 L0 467Z" fill="var(--blue)"/>
      <path d="M0 445 Q170 418 330 440 L330 467 L0 467Z" fill="var(--navy)"/>
    </svg>
    <div class="brand brand--front"><span class="brand__mark brand__mark--small"></span>HARLOW BUILD GROUP</div>
    <div class="tagline"><span class="tagline__lead">BUILDING</span><span class="tagline__rest">A LIFESTYLE</span></div>
    <div class="front-web">www.harlowbuildgroup.example.au</div>
  </div>
  <div class="fold"></div>
</section>

<section class="spread spread--inner" aria-label="Brochure inside">
  <div class="page page--left">
    <svg class="layer" width="330" height="467" viewBox="0 0 330 467">
      <defs>
        <linearGradient id="pondTone" x1="0" y1="0" x2="0" y2="1">
          <stop offset="0" stop-color="#b9c7d3"/>
          <stop offset=".5" stop-color="#5d6b5a"/>
          <stop offset="1" stop-color="#3f8f94"/>
        </linearGradient>
      </defs>
      <polygon role="img" aria-label="Photo of a dark timber home beside a natural swimming pond" points="0,0 330,0 330,215 0,300" fill="url(#pondTone)"/>
      <polygon points="0,175 250,235 0,305" fill="var(--blue)" opacity=".92"/>
      <rect x="0" y="458" width="330" height="9" fill="var(--blue)"/>
    </svg>
    <p class="intro">If you need a quick quality reno, knock-down rebuild or a brand new home talk to us. Together we can plan and create your dream home.</p>
    <div class="section section--build">
      <h2 class="section__title">Create Your New Custom Designed Home</h2>
      <p class="section__sub">New Builds – Single or Multi dwellings</p>
      <p class="section__text">A block of land presents an exciting opportunity to build your dream home. At Harlow we use our expertise and the latest products for a high quality build.</p>
    </div>
    <div class="section section--reno">
      <h2 class="section__title">Transform Your Existing Home</h2>
      <p class="section__sub">Home Renovations and Extensions</p>
      <p class="section__text">Families grow and change over time. So do our living preferences and personal tastes. An extension and bathroom or kitchen renovation can transform your house into the perfect home.</p>
    </div>
  </div>

  <div class="page page--right">
    <svg class="layer" width="330" height="467" viewBox="0 0 330 467">
      <defs>
        <linearGradient id="nightTone" x1="0" y1="0" x2="0" y2="1">
          <stop offset="0" stop-color="#2c3a52"/>
          <stop offset=".6" stop-color="#6d5a4a"/>
          <stop offset="1" stop-color="#3fa3d8"/>
        </linearGradient>
      </defs>
      <polygon role="img" aria-label="Evening photo of a modern home with a lit swimming pool" points="0,235 330,150 330,330 70,330" fill="url(#nightTone)"/>
      <polygon points="0,235 70,330 0,330" fill="var(--sky)"/>
      <rect x="0" y="330" width="330" height="137" fill="var(--blue)"/>
    </svg>
    <div class="team">
      <h2 class="team__title">A Team You Can Trust</h2>
      <p class="team__text">Daniel Harlow and his team take great personal pride in every project. Our team of highly skilled and qualified carpenters and tradespeople will provide you with a quality finished home, on time and on budget.</p>
    </div>
    <p class="consult">We consult with you every step of the way and work closely with your Building Designer or Architect. We offer ongoing advice and support for all aspects of your project.</p>
    <div class="guarantee">
      <h2 class="guarantee__title">Our Guarantee – The Harlow Difference</h2>
      <ul class="guarantee__list">
        <li>Exceptional finished product</li>
        <li>Clean, well presented site throughout the build</li>
        <li>Highest standard of craftsmanship</li>
        <li>Best building experience with the Harlow team</li>
      </ul>
    </div>
    <ul class="guarantee__list guarantee__list--side">
      <li>Open communication and collaboration at all times</li>
    </ul>
    <div class="services">
      <h2 class="services__title">PROFESSIONAL<br>BUILDING SERVICES</h2>
      <p class="services__area">Port Macquarie and the greater Mid North Coast</p>
      <p class="services__licence">INSERT Master Builders Number | ABN | Builders Licence Number</p>
      <p class="services__phones">024719353, 0413597264</p>
      <p class="services__web">www.harlowbuildgroup.example.au</p>
      <div class="services__links">info@harlowbuildgroup.example.au<br>facebook.com/harlowbuildgroup</div>
    </div>
  </div>
  <div class="fold"></div>
</section>

</body>
</html>
```